R&t Subterra

We specialize in CIPP pipe lining but do other underground utilities trenchless as well.

Target Market(s)

Trenchless sewer replacement

Contact Information for Business Card

Gavin Holtby 715-482-6130 Millbrook Falls, wi

```html
<!DOCTYPE html>
<html lang="en">
<head>
<meta charset="utf-8">
<title>R&amp;T Subterra – Business Card</title>
<link rel="stylesheet" href="https://fonts.googleapis.com/css2?family=Poppins:wght@300;400;600;700&display=swap">
<style>
  :root {
    --brand-blue: #2e90cc;
    --ink: #1c1c1c;
    --grey-text: #8a8a8a;
    --card-white: #ffffff;
    --backdrop: #d6d6d6;
  }
  * { margin: 0; padding: 0; box-sizing: border-box; }
  html, body {
    width: 1200px;
    height: 780px;
    overflow: hidden;
    background: var(--backdrop);
    font-family: "Poppins", sans-serif;
  }
  .stage {
    position: relative;
    width: 1200px;
    height: 780px;
    display: flex;
    align-items: center;
    justify-content: center;
    gap: 40px;
  }
  .card {
    position: relative;
    width: 540px;
    height: 310px;
    overflow: hidden;
    box-shadow: 0 10px 28px rgba(0,0,0,0.22);
  }

  /* Front side */
  .card--front { background: var(--card-white); }
  .wordmark {
    position: absolute;
    display: flex;
    align-items: center;
    gap: 10px;
  }
  .wordmark__dot {
    border-radius: 50%;
    flex: none;
  }
  .wordmark__name {
    font-weight: 700;
    letter-spacing: 0.5px;
    white-space: nowrap;
  }
  .card--front .wordmark { right: 36px; top: 36px; }
  .card--front .wordmark__dot { width: 34px; height: 34px; background: var(--brand-blue); }
  .card--front .wordmark__name { font-size: 30px; color: var(--brand-blue); }

  .person {
    position: absolute;
    right: 48px;
    top: 128px;
    text-align: right;
  }
  .person__name {
    font-size: 34px;
    line-height: 1.1;
    white-space: nowrap;
  }
  .person__first { font-weight: 700; color: var(--brand-blue); }
  .person__last { font-weight: 300; color: var(--grey-text); }
  .person__role {
    font-size: 15px;
    font-weight: 400;
    color: var(--ink);
    margin-top: 2px;
  }
  .accent-bar {
    position: absolute;
    right: 0;
    top: 136px;
    width: 26px;
    height: 74px;
    background: var(--brand-blue);
  }
  .contact {
    position: absolute;
    right: 30px;
    bottom: 26px;
    list-style: none;
    text-align: right;
  }
  .contact__item {
    display: flex;
    align-items: center;
    justify-content: flex-end;
    gap: 8px;
    font-size: 15px;
    color: var(--ink);
    line-height: 1.6;
  }
  .contact__icon { width: 14px; height: 14px; flex: none; }

  /* Back side */
  .card--back { background: var(--brand-blue); }
  .card--back .wordmark {
    left: 50%;
    top: 50%;
    transform: translate(-50%, -50%);
    gap: 16px;
  }
  .card--back .wordmark__dot { width: 52px; height: 52px; background: var(--card-white); }
  .card--back .wordmark__name { font-size: 44px; color: var(--card-white); }
</style>
</head>
<body>
<main class="stage">

  <section class="card card--front" aria-label="Business card front">
    <div class="wordmark">
      <span class="wordmark__dot" aria-hidden="true"></span>
      <span class="wordmark__name">R&amp;T SUBTERRA</span>
    </div>

    <div class="person">
      <p class="person__name"><span class="person__first">Gavin</span> <span class="person__last">Holtby</span></p>
      <p class="person__role">Sewer and Water Specialists</p>
    </div>
    <div class="accent-bar" aria-hidden="true"></div>

    <ul class="contact">
      <li class="contact__item">
        <span>715-482-6130</span>
        <svg class="contact__icon" viewBox="0 0 24 24" aria-hidden="true">
          <path d="M6.6 10.8a15.1 15.1 0 0 0 6.6 6.6l2.2-2.2a1 1 0 0 1 1-.25 11.4 11.4 0 0 0 3.6.57 1 1 0 0 1 1 1V20a1 1 0 0 1-1 1A17 17 0 0 1 3 4a1 1 0 0 1 1-1h3.5a1 1 0 0 1 1 1c0 1.25.2 2.45.57 3.57a1 1 0 0 1-.25 1z" fill="var(--brand-blue)"/>
        </svg>
      </li>
      <li class="contact__item">
        <span>Millbrook Falls, wi</span>
        <svg class="contact__icon" viewBox="0 0 24 24" aria-hidden="true">
          <path d="M12 2a7 7 0 0 0-7 7c0 5 7 13 7 13s7-8 7-13a7 7 0 0 0-7-7zm0 9.5A2.5 2.5 0 1 1 12 6.5a2.5 2.5 0 0 1 0 5z" fill="var(--brand-blue)"/>
        </svg>
      </li>
    </ul>
  </section>

  <section class="card card--back" aria-label="Business card back">
    <div class="wordmark">
      <span class="wordmark__dot" aria-hidden="true"></span>
      <span class="wordmark__name">R&amp;T SUBTERRA</span>
    </div>
  </section>

</main>
</body>
</html>
```